Mbeleko & Tumusiime Advocates website

An interactive professional law firm website fully synchronized with social media pages.

Target Market(s)

Corporations and professionals

Industry/Entity Type

Professional Service

Number of Pages Required

5+ page

Font styles to use
Sans Serif

Colors

Designer to choose colors to be used in the design.

```html
<!DOCTYPE html>
<html lang="en">
<head>
<meta charset="utf-8">
<title>Mbeleko &amp; Tumusiime Advocates</title>
<link rel="stylesheet" href="https://fonts.googleapis.com/css2?family=Roboto:wght@400;500;700&family=Roboto+Slab:wght@400;700&display=swap">
<style>
:root{
  --red:#8e1b1f;
  --red-dark:#6f1317;
  --ink:#2a2a2a;
  --muted:#666;
  --line:#e2e2e2;
  --soft:#f4f4f4;
  --footer:#2e2e2e;
  --footer-deep:#222;
  --white:#fff;
}
*{box-sizing:border-box;margin:0;padding:0}
html,body{width:1200px;height:3780px;overflow:hidden;background:var(--white)}
body{position:relative;font-family:"Roboto Slab",serif;color:var(--ink)}
.abs{position:absolute}
.btn{position:absolute;display:inline-block;background:var(--red);color:var(--white);font:700 14px "Roboto",sans-serif;letter-spacing:1px;padding:10px 26px;border-radius:3px}
.ph{position:absolute}
/* header */
.site-header{position:absolute;left:0;top:0;width:1200px;height:190px;background:var(--white)}
.brand{position:absolute;left:120px;top:36px;display:flex;align-items:center;gap:14px}
.brand-mark{width:54px;height:54px;background:var(--red)}
.brand-name{font:500 22px/1.2 "Roboto",sans-serif;color:var(--ink)}
.nav{position:absolute;left:120px;top:148px;width:960px;display:flex;justify-content:space-between;font:500 15px "Roboto",sans-serif;color:var(--ink)}
.nav .active{color:var(--red);border-bottom:3px solid var(--red);padding-bottom:10px}
/* hero */
.hero{position:absolute;left:0;top:190px;width:1200px;height:580px;background:linear-gradient(160deg,#e9eef3 0%,#c6cfd8 45%,#8f9aa6 100%)}
.hero-title{position:absolute;left:0;top:255px;width:1200px;text-align:center;font:700 44px "Roboto",sans-serif;color:var(--white)}
.arrow{position:absolute;width:34px;height:34px;border-radius:50%;background:var(--footer-deep)}
.arrow.red{background:var(--red)}
.stats{position:absolute;left:0;top:420px;width:1200px;height:160px;background:rgba(30,30,30,.82);display:flex;justify-content:space-between;padding:30px 120px 0}
.stat{width:220px;text-align:center;color:var(--white);font-family:"Roboto",sans-serif}
.stat svg{display:block;margin:0 auto 10px}
.stat-label{font:700 17px "Roboto",sans-serif;letter-spacing:1px}
.stat-value{font:400 18px "Roboto",sans-serif;margin-top:6px}
/* intro */
.intro{position:absolute;left:0;top:820px;width:1200px;height:390px;border-bottom:1px solid var(--line)}
.intro h2,.practice h3{font:400 28px "Roboto Slab",serif;color:var(--ink)}
.intro p,.practice p{font:400 13px/1.55 "Roboto Slab",serif;color:var(--muted)}
/* practice */
.practice-card{position:absolute;top:1240px;width:300px;height:520px}
.practice h3{font:700 18px "Roboto",sans-serif;letter-spacing:.5px;margin:24px 0 8px}
/* professionals */
.pros{position:absolute;left:0;top:1820px;width:1200px;height:540px;background:radial-gradient(ellipse at 50% 55%,#6a4b30 0%,#3b2616 45%,#1a110a 100%)}
.pros h2{position:absolute;left:0;top:220px;width:1200px;text-align:center;font:400 42px "Roboto Slab",serif;color:var(--white)}
.pros .sub{position:absolute;left:0;top:278px;width:1200px;text-align:center;font:400 13px "Roboto",sans-serif;color:#e4d8cc}
/* team */
.team-title{position:absolute;left:0;top:2410px;width:1200px;text-align:center;font:400 32px "Roboto Slab",serif}
.team-sub{position:absolute;left:0;top:2460px;width:1200px;text-align:center;font:400 13px "Roboto",sans-serif;color:var(--muted)}
.member{position:absolute;top:2520px;width:192px;text-align:center}
.member .ph{position:relative;width:192px;height:300px;background:linear-gradient(180deg,#7d8792 0%,#3d434b 100%)}
.socials{display:flex;justify-content:center;gap:8px;margin-top:20px}
.socials span{width:22px;height:22px;border-radius:50%;background:#3a3a3a}
.member .name{font:700 18px "Roboto Slab",serif;margin-top:30px}
.member .role{font:400 16px "Roboto Slab",serif;color:var(--muted);margin-top:16px}
.dots{position:absolute;top:3080px;left:578px;display:flex;gap:10px}
.dots span{width:10px;height:10px;border-radius:50%;background:#ccc}
.dots span.on{background:var(--red)}
/* clients */
.clients{position:absolute;left:0;top:3120px;width:1200px;height:320px;background:var(--soft)}
.tab{position:absolute;top:26px;text-align:center;font:400 22px/1.25 "Roboto",sans-serif;color:#444}
.tab.on{color:var(--red);border-bottom:3px solid var(--red);padding-bottom:8px}
.logo-tile{position:absolute;top:136px;width:118px;height:100px;background:var(--white);border:1px solid var(--line);display:flex;align-items:center;justify-content:center;text-align:center;font:700 14px "Roboto",sans-serif;color:var(--red);padding:6px}
/* footer */
.site-footer{position:absolute;left:0;top:3440px;width:1200px;height:280px;background:var(--footer);color:#cfcfcf;font:400 13px/1.7 "Roboto",sans-serif}
.site-footer h4{font:700 15px "Roboto",sans-serif;color:var(--white);margin-bottom:12px}
.f-col{position:absolute;top:40px}
.f-brand{display:flex;align-items:center;gap:12px;background:var(--white);padding:10px 14px;width:250px}
.f-brand .brand-mark{width:40px;height:40px}
.f-brand .brand-name{font-size:16px}
.field{height:32px;background:#444;border:1px solid #555;margin-bottom:10px;color:#aaa;font-size:12px;padding:6px 10px}
.copy{position:absolute;left:0;top:3720px;width:1200px;height:60px;background:var(--footer-deep);color:#bbb;font:400 13px "Roboto",sans-serif;padding:22px 120px}
.copy .socials{position:absolute;right:120px;top:18px;margin:0}
.copy .socials span{background:var(--red)}
</style>
</head>
<body>

<header class="site-header">
  <div class="brand"><span class="brand-mark"></span><span class="brand-name">Mbeleko &amp; Tumusiime<br>Advocates</span></div>
  <nav class="nav">
    <span class="active">Home</span><span>Our History</span><span>Who We Are</span><span>How We Do It</span><span>Practice Areas</span><span>Our Clients</span><span>Our Professionals</span><span>Contact</span>
  </nav>
</header>

<section class="hero">
  <div class="ph" role="img" aria-label="Modern glass office building against a pale sky" style="left:0;top:0;width:1200px;height:580px;background:linear-gradient(160deg,#eef2f6 0%,#c9d2db 50%,#8c97a3 100%)"></div>
  <span class="arrow" style="left:40px;top:162px"></span>
  <span class="arrow red" style="left:1126px;top:162px"></span>
  <h1 class="hero-title">Qualified Legal Advice</h1>
  <span class="btn" style="left:540px;top:322px">VIEW MORE</span>
  <div class="stats">
    <div class="stat">
      <svg width="40" height="30" viewBox="0 0 40 30"><path d="M4 18l10-8 6 4 6-4 10 8-10 8-6-4-6 4z" fill="none" stroke="#fff" stroke-width="2"/></svg>
      <div class="stat-label">PARTNERS</div><div class="stat-value">5</div>
    </div>
    <div class="stat">
      <svg width="40" height="30" viewBox="0 0 40 30"><circle cx="14" cy="9" r="5" fill="#fff"/><circle cx="27" cy="9" r="5" fill="#fff"/><path d="M4 28c0-8 20-8 20 0zM18 28c0-8 20-8 20 0z" fill="#fff"/></svg>
      <div class="stat-label">PEOPLE</div><div class="stat-value">20+</div>
    </div>
    <div class="stat">
      <svg width="40" height="30" viewBox="0 0 40 30"><rect x="8" y="3" width="24" height="25" fill="none" stroke="#fff" stroke-width="2"/><path d="M13 11h14M13 17h14M13 23h9" stroke="#fff" stroke-width="2"/></svg>
      <div class="stat-label">COMBINED EXPERIENCE</div><div class="stat-value">65</div>
    </div>
    <div class="stat">
      <svg width="40" height="30" viewBox="0 0 40 30"><circle cx="20" cy="15" r="12" fill="none" stroke="#fff" stroke-width="2"/><path d="M14 15l4 5 8-9" fill="none" stroke="#fff" stroke-width="2.5"/></svg>
      <div class="stat-label">CASES SOLVED</div><div class="stat-value">300+</div>
    </div>
  </div>
</section>

<section class="intro">
  <div class="abs" style="left:120px;top:74px;width:250px">
    <h2>Our History</h2>
    <p style="margin-top:22px">In 1990, our firm was founded and is comprised of 8 Partners and over 20 Associates and support staff fully engaged and focused on client service. The firm is fully automated and is on the latest practice management software with efficient client focused delivery systems and improved turnaround times.</p>
  </div>
  <span class="btn" style="left:120px;top:326px">View More</span>
  <div class="abs" style="left:400px;top:74px;width:260px">
    <h2>Who We Are</h2>
    <p style="margin-top:22px">Mbeleko &amp; Tumusiime Advocates are a specialist commercial law firm in Uganda focusing on commercial litigation, construction law and arbitration. We have excelled in our niche over the years, and we continue to grow and be the first choice in these practice areas.</p>
  </div>
  <span class="btn" style="left:400px;top:326px">View More</span>
  <div class="ph" role="img" aria-label="Group photo of the firm's partners and staff in suits" style="left:690px;top:70px;width:390px;height:290px;background:linear-gradient(180deg,#b9a98f 0%,#5a4e45 100%)"></div>
</section>

<section class="practice">
  <div class="practice-card" style="left:120px">
    <div class="ph" role="img" aria-label="Construction site with steel scaffolding" style="position:relative;width:300px;height:232px;background:linear-gradient(180deg,#c9c7c2 0%,#6d6a64 100%)"></div>
    <h3>CONSTRUCTION LAW</h3>
    <p>Our Construction Law Department is headed by our Senior Partner who is highly qualified and experienced in construction law and in providing advice.</p>
    <span class="btn" style="left:0;top:440px">View More</span>
  </div>
  <div class="practice-card" style="left:450px">
    <div class="ph" role="img" aria-label="Lawyer reviewing documents at a desk" style="position:relative;width:300px;height:232px;background:linear-gradient(180deg,#9aa3ad 0%,#3f454c 100%)"></div>
    <h3>COMMERCIAL LITIGATION</h3>
    <p>Our Commercial Litigation Department is headed by our Senior Partner who is highly qualified and experienced in commercial disputes and advice.</p>
    <span class="btn" style="left:0;top:440px">View More</span>
  </div>
  <div class="practice-card" style="left:780px">
    <div class="ph" role="img" aria-label="Gavel on a desk beside a signing hand" style="position:relative;width:300px;height:232px;background:linear-gradient(180deg,#a49382 0%,#3b2f27 100%)"></div>
    <h3>ARBITRATION</h3>
    <p>Our Arbitration Department is headed by our Senior Partner who is highly qualified and experienced in arbitration matters and in providing advice.</p>
    <span class="btn" style="left:0;top:440px">View More</span>
  </div>
</section>

<section class="pros">
  <div class="ph" role="img" aria-label="Scales of justice, law books and a gavel on a dark desk" style="left:0;top:0;width:1200px;height:540px;background:radial-gradient(ellipse at 50% 55%,#6a4b30 0%,#3b2616 45%,#1a110a 100%)"></div>
  <h2>Our Professionals</h2>
  <p class="sub">Trusted counsel for every stage of your business</p>
  <span class="btn" style="left:538px;top:312px">View More</span>
</section>

<h2 class="team-title">Our Team</h2>
<p class="team-sub">Experienced advocates serving our clients</p>

<div class="member" style="left:120px">
  <div class="ph" role="img" aria-label="Portrait of the managing partner"></div>
  <div class="socials"><span></span><span></span><span></span></div>
  <div class="name">Peter N. Mbeleko</div><div class="role">Managing Partner</div>
</div>
<div class="member" style="left:372px">
  <div class="ph" role="img" aria-label="Portrait of the senior partner"></div>
  <div class="socials"><span></span><span></span><span></span></div>
  <div class="name">Ronald A. Tumusiime</div><div class="role">Senior Partner</div>
</div>
<div class="member" style="left:632px">
  <div class="ph" role="img" aria-label="Portrait of a partner"></div>
  <div class="socials"><span></span><span></span><span></span></div>
  <div class="name">Grace Atuhaire</div><div class="role">Partner</div>
</div>
<div class="member" style="left:884px">
  <div class="ph" role="img" aria-label="Portrait of the managing partner"></div>
  <div class="socials"><span></span><span></span><span></span></div>
  <div class="name">Samuel Okello</div><div class="role">Managing Partner</div>
</div>
<div class="dots"><span class="on"></span><span></span><span></span></div>

<section class="clients">
  <div class="tab" style="left:120px;width:240px">Construction<br>&amp; Arbitration</div>
  <div class="tab on" style="left:470px;width:260px">Commercial Litigation<br>&amp; Transactions</div>
  <div class="tab" style="left:860px;width:220px">Corporate<br>Advisory</div>
  <span class="arrow" style="left:40px;top:170px"></span>
  <span class="arrow" style="left:1126px;top:170px"></span>
  <div class="logo-tile" style="left:120px">Northway Freight</div>
  <div class="logo-tile" style="left:260px">Harvest Lane</div>
  <div class="logo-tile" style="left:400px">Crestline</div>
  <div class="logo-tile" style="left:540px">Kivu Mutual</div>
  <div class="logo-tile" style="left:680px">Boxwell</div>
  <div class="logo-tile" style="left:820px">Lakeside Co</div>
  <div class="logo-tile" style="left:960px">Summit Group</div>
</section>

<footer class="site-footer">
  <div class="f-col" style="left:120px;width:260px">
    <div class="f-brand"><span class="brand-mark"></span><span class="brand-name">Mbeleko &amp; Tumusiime<br>Advocates</span></div>
    <p style="margin-top:16px">A specialist commercial law firm offering clear, practical legal advice to businesses across the region.</p>
    <p style="margin-top:8px;color:#fff">Read More &rsaquo;</p>
  </div>
  <div class="f-col" style="left:420px;width:180px">
    <h4>Head Office Address</h4>
    <p>Plot 14 Nile Crescent,<br>2nd Floor, Unity House<br>P.O. Box 1024<br>Kampala, Uganda</p>
  </div>
  <div class="f-col" style="left:620px;width:200px">
    <h4>Contacts</h4>
    <p>T: +256 700 555 014<br>M: +256 772 555 208<br>E: office@mbelekotumusiime.example<br>W: www.mbelekotumusiime.example</p>
  </div>
  <div class="f-col" style="left:850px;width:230px">
    <h4>Quick Contact</h4>
    <div style="display:flex;gap:10px"><div class="field" style="flex:1">Name</div><div class="field" style="flex:1">Phone</div></div>
    <div class="field" style="height:60px">Message</div>
    <span class="btn" style="position:relative;float:right;padding:6px 18px;font-size:12px">Send</span>
  </div>
</footer>

<div class="copy">Copyright &copy; 2018 Mbeleko &amp; Tumusiime Advocates. All Rights Reserved.
  <div class="socials"><span></span><span></span><span></span><span></span><span></span></div>
</div>

</body>
</html>
```